YOU Campaign. Recruitment for Graduating Optometrist

Mobile Healthcare Company for OptometryPlease see attachment for my YOU campaign and any postcard size will work if we can get most of the details off the word document and I would like a pair of eye-glasses between the you on the title. This Campaign is for graduating class of 2016 in May for Optometrist and we want to entice them to enjoy our company and attend the Plantor event and come visit our booth in the exhibit hall.

Target Market(s)

Optometrist who ate graduating from Optometry School in May 2016

Industry/Entity Type

Health And Wellness

Font styles to use
Serif
Sans Serif
Decorative
Script

Requirements
Must have
• Eye glasses and Optometry theme
• view website www.brightkinder.example
Nice to have
• mobile Optometry equipment, glasses, you in shadow backgrounds
• colorful, kids
Should not have
• dark themes and bad grammar

```html
<!DOCTYPE html>
<html lang="en">
<head>
<meta charset="utf-8">
<title>YOU Campaign – Optometrist Recruitment Postcard</title>
<link href="https://fonts.googleapis.com/css2?family=Alfa+Slab+One&family=Open+Sans:wght@400;600;700&display=swap" rel="stylesheet">
<style>
  :root{
    --stage:#e9eaec;
    --paper:#fbfbfb;
    --chart-grey:#8d8d8d;
    --sky-blue:#2b8ae2;
    --navy-blue:#1d58b0;
    --orange:#e8731f;
    --frame-orange:#ef8a2e;
    --text:#222;
  }
  *{box-sizing:border-box;margin:0;padding:0}
  html,body{width:1200px;height:1000px;overflow:hidden;background:var(--stage)}
  body{position:relative;font-family:"Open Sans",Arial,sans-serif;color:var(--text)}

  .card{position:absolute;background:var(--paper);box-shadow:0 4px 18px rgba(0,0,0,.18)}

  /* ---------- back of postcard ---------- */
  .card-back{left:24px;top:190px;width:604px;height:640px;padding:30px 28px 26px;display:flex;gap:24px}
  .card-back .col{flex:1;min-width:0;font-size:12.2px;line-height:1.45}
  .card-back p{margin-bottom:10px}
  .eyes-heading{font-family:"Alfa Slab One",Georgia,serif;font-weight:400;color:var(--navy-blue);font-size:22px;line-height:1.05;margin-bottom:14px;text-transform:uppercase}
  .eyes-heading .accent{color:var(--orange);font-size:30px}
  .brand-inline{font-weight:700;color:var(--navy-blue)}
  .benefit{font-weight:700;color:var(--navy-blue)}
  .benefit-list p{margin-bottom:6px}
  .believe{font-family:"Alfa Slab One",Georgia,serif;color:var(--orange);font-size:14px;line-height:1.2}
  .brand-mark{display:flex;align-items:center;gap:6px;color:var(--navy-blue);font-weight:600;font-size:19px;margin:8px 0 8px}
  .brand-mark .dot{width:13px;height:13px;background:var(--navy-blue)}
  .contact{font-weight:700;color:var(--navy-blue);font-size:12.5px;line-height:1.45}
  .website{font-weight:700;color:var(--orange);font-size:13px}

  /* ---------- front of postcard ---------- */
  .card-front{left:650px;top:30px;width:520px;height:940px;text-align:center;overflow:hidden}
  .chart-e{font-family:"Alfa Slab One",Georgia,serif;font-size:170px;line-height:1;margin-top:22px;
    background:linear-gradient(#0d0d0d 45%,#8a8a8a);-webkit-background-clip:text;background-clip:text;color:transparent}
  .tagline{color:var(--sky-blue);font-weight:700;font-size:16px;line-height:1.35}
  .lead{display:flex;justify-content:center;align-items:center;gap:6px;margin-top:4px}
  .lead .brand-mark{color:var(--sky-blue);font-size:17px;font-weight:600;margin:0}
  .lead .brand-mark .dot{background:var(--sky-blue)}
  .you{font-family:"Alfa Slab One",Georgia,serif;color:var(--sky-blue);font-size:96px;line-height:1.02;margin-top:2px}
  .chart-row{font-family:"Alfa Slab One",Georgia,serif;color:var(--chart-grey);letter-spacing:.42em;padding-left:.42em;line-height:1}
  .row-1{font-size:56px;margin-top:6px}
  .row-2{font-size:42px;margin-top:6px}
  .row-3{font-size:34px;margin-top:6px}
  .row-4{font-size:25px;margin-top:8px;color:#6f6f6f}
  .row-5{font-size:19px;margin-top:14px;color:#333}
  .row-6{font-size:15px;margin-top:12px;color:#222}
  .row-7{font-size:12px;margin-top:12px;color:#222}
  .row-8{font-size:10px;margin-top:10px;color:#222}
  .tagline.small{margin-top:4px}
  .glasses-photo{position:absolute;left:0;right:0;bottom:0;height:220px;
    background:radial-gradient(ellipse 70% 45% at 50% 45%,rgba(239,138,46,.85),rgba(239,138,46,.35) 60%,rgba(251,251,251,0) 80%),var(--paper)}
</style>
</head>
<body>

<section class="card card-back" aria-label="Postcard back">
  <div class="col">
    <h2 class="eyes-heading">We have our<br>eyes on <span class="accent">YOU!</span></h2>
    <p><span class="brand-inline">Bright Kinder</span> has grown into the largest school health care provider in the state of Tennessee providing an array of services to more than thirty school districts in Tennessee. Our practice uses state of the art technology, and we have a great staff to assist in work up and patient care.</p>
    <p>We are looking for full-time and part-time Optometrists interested in working in Memphis and Nashville Tennessee anywhere from 1 to 5 days a week. Great hours! No nights, weekends, or holidays, school hours and days only. Benefits include:</p>
    <div class="benefit-list">
      <p><span class="benefit">Bonus structure</span> based upon productivity and attendance that adds upwards of $17,000-$23,000 per year to your compensation</p>
      <p><span class="benefit">42 paid days off</span> during the calendar year: a minimum of 5 weeks in the summer, 2 weeks for Christmas break, 4 paid holidays and 3 personal days</p>
      <p><span class="benefit">Sign-on bonus</span> of $5,000</p>
    </div>
  </div>
  <div class="col">
    <p><span class="brand-inline">Bright Kinder</span> believes in empowering those we work with to do what's right, and to put patient needs and quality of care above all. We surround ourselves with people who are committed to creating happiness every day, and who are energized to serve those we are uniquely qualified to help.</p>
    <p><span class="believe">We believe that YOU are our candidate!!!</span> Please contact us if you're interested in joining our team and we can discuss our complete benefit package, competitive compensation and what working for <span class="brand-inline">Bright Kinder</span> brings to you!</p>
    <p>We look forward to speaking with you at the Plantor event!</p>
    <div class="brand-mark"><span class="dot"></span>Bright Kinder</div>
    <p class="contact">Contact Marisa Cole at<br>mcole@brightkinder.example<br>901 555-0142 ex. 210</p>
    <p class="website">www.brightkinder.example</p>
  </div>
</section>

<section class="card card-front" aria-label="Postcard front">
  <div class="chart-e">E</div>
  <div class="lead">
    <div class="brand-mark"><span class="dot"></span>Bright Kinder</div>
    <span class="tagline">has 20-20 vision and believes that</span>
  </div>
  <div class="you">YOU</div>
  <p class="tagline">are our candidate!!!</p>
  <div class="chart-row row-1">TOZ</div>
  <p class="tagline">We are looking for full-time and part-time optometrists</p>
  <div class="chart-row row-2">LPED</div>
  <p class="tagline small">interested in working in</p>
  <div class="chart-row row-3">PECFD</div>
  <p class="tagline small">Memphis and Nashville Tennessee</p>
  <div class="chart-row row-4">EDFCZP</div>
  <div class="chart-row row-5">FELOPZD</div>
  <div class="chart-row row-6">DEFPOTEC</div>
  <div class="chart-row row-7">LEFODPCT</div>
  <div class="chart-row row-8">FDPLTCEO</div>
  <div class="glasses-photo" role="img" aria-label="Photo of round orange eyeglasses resting in front of the eye chart"></div>
</section>

</body>
</html>
```